Copper Meadow Creamery Business cards

We need a logo design for our family dairy. Included on the cards should be my name/my husbands name/the dairy name/ all the phone numbers/address and email. The name is Copper Meadow Creamery, LLC. We would like to use our farm mascot pic on the card. We know the pictures I sent you are of a beef cow but she is the mascot of the farm. We were thinking that maybe put a picture of her head in the middle of the card with a "B" on one side and a "D" on the other side with a "C" around the picture of the cow. But we are open to any ideas. We are looking for something kind of professional and a design that that can be used on cards, clothing and a car sign. Black lettering and blue for the other color...or what looks good.

Target Market(s)

All

Industry/Entity Type

Farming

Contact Information for Business Card

Marla Dutton Owner (555)417-2093
Ronald Pfister Owner (555)238-7715
Copper Meadow Creamery, LLC (555)906-4182
Coppermeadowcreamery@mailbarn.test
7126 County Lane 91, Alderbrook, MN 50917

Font styles to use
Sans Serif

Colors
3176b5
3c7bb8
3277b5
0255a3

Requirements
Must have
• Some design that incorporates a drawing/pic of the cow pictures that were sent.
Nice to have
• no suggestions
Should not have
• no suggestions

```html
<!DOCTYPE html>
<html lang="en">
<head>
<meta charset="utf-8">
<title>Copper Meadow Creamery — Business Cards</title>
<link rel="stylesheet" href="https://fonts.googleapis.com/css2?family=Source+Sans+3:wght@400;600;700&display=swap">
<style>
  :root {
    --page-bg: #ececec;
    --card-blue: #0255a3;
    --band-blue: #003f80;
    --text-white: #ffffff;
    --rule-white: rgba(255,255,255,0.75);
  }
  * { margin: 0; padding: 0; box-sizing: border-box; }
  html, body { width: 1200px; height: 900px; overflow: hidden; }
  body {
    background: var(--page-bg);
    font-family: "Source Sans 3", Arial, sans-serif;
    color: var(--text-white);
    position: relative;
  }
  .card {
    position: absolute;
    background: var(--card-blue);
    overflow: hidden;
  }
  .band { position: absolute; left: 0; right: 0; background: var(--band-blue); }

  /* Contact side */
  .card-contact { left: 78px; top: 35px; width: 588px; height: 362px; }
  .card-contact .band-top { top: 0; height: 48px; }
  .card-contact .band-bottom { bottom: 0; height: 48px; }
  .owner { position: absolute; top: 88px; }
  .owner-name { font-size: 23px; font-weight: 600; line-height: 1.2; }
  .owner-title, .owner-phone { font-size: 16px; line-height: 1.55; }
  .owner-left { right: 316px; text-align: right; }
  .owner-right { left: 318px; text-align: left; }
  .owner-phone { display: flex; align-items: center; gap: 6px; }
  .owner-left .owner-phone { justify-content: flex-end; }
  .phone-icon { width: 12px; height: 12px; fill: var(--text-white); }

  .company-block { position: absolute; left: 0; right: 0; top: 193px; text-align: center; }
  .company-line { display: flex; align-items: center; justify-content: center; gap: 8px; font-size: 17px; font-weight: 600; }
  .company-line .rule { width: 66px; height: 1px; background: var(--rule-white); }
  .address { font-size: 18px; margin-top: 1px; }
  .reach { font-size: 15.5px; margin-top: 10px; }
  .reach .divider { margin: 0 6px; }

  /* Logo side */
  .card-logo { left: 388px; top: 505px; width: 567px; height: 352px; }
  .card-logo .band-top { top: 0; height: 85px; }
  .card-logo .band-bottom { bottom: 0; height: 84px; }
  .brand {
    position: absolute; left: 0; right: 0; top: 85px; height: 183px;
    display: flex; align-items: center; justify-content: center; gap: 16px;
  }
  .brand-mark { width: 46px; height: 46px; border-radius: 50%; background: var(--text-white); flex: none; }
  .brand-name { font-size: 38px; font-weight: 700; line-height: 1.05; letter-spacing: 0.5px; text-transform: uppercase; }
</style>
</head>
<body>
  <section class="card card-contact">
    <div class="band band-top"></div>
    <div class="band band-bottom"></div>

    <div class="owner owner-left">
      <div class="owner-name">Ronald Pfister</div>
      <div class="owner-title">Owner</div>
      <div class="owner-phone">(555)238-7715
        <svg class="phone-icon" viewBox="0 0 24 24" aria-hidden="true"><path d="M6.6 10.8a15.1 15.1 0 0 0 6.6 6.6l2.2-2.2c.3-.3.7-.4 1-.2 1.1.4 2.3.6 3.6.6.6 0 1 .4 1 1V20c0 .6-.4 1-1 1C10.6 21 3 13.4 3 4c0-.6.4-1 1-1h3.5c.6 0 1 .4 1 1 0 1.3.2 2.5.6 3.6.1.3 0 .7-.2 1z"/></svg>
      </div>
    </div>

    <div class="owner owner-right">
      <div class="owner-name">Marla Dutton</div>
      <div class="owner-title">Owner</div>
      <div class="owner-phone">
        <svg class="phone-icon" viewBox="0 0 24 24" aria-hidden="true"><path d="M6.6 10.8a15.1 15.1 0 0 0 6.6 6.6l2.2-2.2c.3-.3.7-.4 1-.2 1.1.4 2.3.6 3.6.6.6 0 1 .4 1 1V20c0 .6-.4 1-1 1C10.6 21 3 13.4 3 4c0-.6.4-1 1-1h3.5c.6 0 1 .4 1 1 0 1.3.2 2.5.6 3.6.1.3 0 .7-.2 1z"/></svg>
        (555)417-2093</div>
    </div>

    <div class="company-block">
      <div class="company-line"><span class="rule"></span>Copper Meadow Creamery, LLC<span class="rule"></span></div>
      <div class="address">7126 County Lane 91 Alderbrook, MN 50917</div>
      <div class="reach">(555)906-4182<span class="divider">|</span>Coppermeadowcreamery@mailbarn.test</div>
    </div>
  </section>

  <section class="card card-logo">
    <div class="band band-top"></div>
    <div class="band band-bottom"></div>
    <div class="brand">
      <span class="brand-mark"></span>
      <span class="brand-name">Copper Meadow<br>Creamery, LLC</span>
    </div>
  </section>
</body>
</html>
```